Powerpoint template for Presenting Java Related Training

I am launching a website in 2017 called Kestrel Code Clinics that will offer training on advanced topics in Java programming. I need a Powerpoint template for use in the training courses. I have attached my logo. I am also attaching my business card design which was just completed ... I'd like to stay somewhat consistent between the different media, but without making the Powerpoint template too busy.
Updates

Project Deadline Extended Reason: Only 3 designs received and 2 days left so I am extending the deadline by 5 days. I would like to have at least 5 or 6 designs to consider before I make my decision. Added Sunday, October 30, 2016

Target Market(s)

Current and Prospective Software Developers

Industry/Entity Type

Software

Font styles to use
Serif
Sans Serif

Requirements
Must have
• Must use the provided logo and must use a color scheme that works well with the logo provided. Must be easy to read since this is for a training presentation and I don't want any distractions from the content.
Nice to have
• I would like to have alternatives for different types of content ... e.g. bullet lists vs. graphics, etc.
Should not have
• Just not too busy ... I want something that looks distinctive and nice but with minimal distractions.

```html
<!DOCTYPE html>
<html lang="en">
<head>
<meta charset="utf-8">
<title>Kestrel Code Clinics – Chart Slide</title>
<link rel="stylesheet" href="https://fonts.googleapis.com/css2?family=Roboto:wght@400;700&family=Open+Sans:wght@400&display=swap">
<style>
  :root {
    --brand-red: #EE3237;
    --brand-blue: #0F71B5;
    --bar-red: #D7383E;
    --bar-teal: #1BB5A0;
    --bar-orange: #EE720E;
    --ink-grey: #555555;
    --label-grey: #7a7a7a;
    --grid: #d9d9d9;
    --white: #ffffff;
  }
  html, body { margin: 0; padding: 0; overflow: hidden; background: var(--white); }
  .slide {
    position: relative; width: 1200px; height: 675px; overflow: hidden;
    background: var(--white); font-family: "Open Sans", Arial, sans-serif;
  }
  .side-panel {
    position: absolute; left: 0; top: 0; width: 342px; height: 675px;
    background: var(--brand-red);
  }
  .brand-decoration {
    position: absolute; left: 0; top: 0; width: 342px; height: 420px;
    background: linear-gradient(215deg, var(--brand-blue) 0%, var(--brand-blue) 30%, var(--brand-red) 75%);
    display: flex; align-items: flex-start; justify-content: flex-start;
  }
  .brand-name {
    margin: 34px 0 0 34px; color: var(--white);
    font-family: "Roboto", Arial, sans-serif; font-weight: 700; font-size: 18px;
  }
  .slide-title {
    position: absolute; left: 34px; top: 448px; margin: 0;
    color: var(--white); font-family: "Roboto", Arial, sans-serif;
    font-weight: 700; font-size: 46px; line-height: 54px; letter-spacing: -1.2px;
  }
  .slide-date {
    position: absolute; left: 35px; top: 636px; color: var(--white);
    font-family: "Roboto", Arial, sans-serif; font-size: 13px;
  }
  .slide-footer {
    position: absolute; left: 390px; top: 636px; color: var(--brand-blue);
    font-family: "Roboto", Arial, sans-serif; font-size: 13px;
  }
  .page-number {
    position: absolute; right: 12px; top: 635px; color: var(--brand-blue);
    font-family: "Roboto", Arial, sans-serif; font-weight: 700; font-size: 14px;
  }
  .accent-bar {
    position: absolute; right: 0; top: 75px; width: 37px; height: 524px;
    background: var(--brand-blue);
  }
  .chart { position: absolute; left: 0; top: 0; }
  .chart-title { font-size: 24px; fill: var(--ink-grey); letter-spacing: 0.5px; }
  .legend-text { font-size: 13px; fill: var(--ink-grey); }
  .value-label { font-size: 11px; fill: var(--label-grey); }
  .category-label { font-size: 12px; fill: var(--ink-grey); letter-spacing: 2px; }
  .grid-line { stroke: var(--grid); stroke-width: 1; }
  .s1 { fill: var(--bar-red); }
  .s2 { fill: var(--bar-teal); }
  .s3 { fill: var(--bar-orange); }
</style>
</head>
<body>
<main class="slide">
  <aside class="side-panel">
    <div class="brand-decoration" role="img" aria-label="Brand swoosh decoration in red and blue">
      <span class="brand-name">Kestrel Code Clinics</span>
    </div>
    <h1 class="slide-title">Slide title<br>template</h1>
    <div class="slide-date">29.10.2016</div>
  </aside>

  <svg class="chart" width="1200" height="675" viewBox="0 0 1200 675" aria-label="Sample graph bar chart">
    <text class="chart-title" x="744" y="115" text-anchor="middle">SAMPLE GRAPH</text>
    <g class="legend">
      <rect class="s1" x="626" y="138" width="7" height="7"/><text class="legend-text" x="636" y="147">Sample 1</text>
      <rect class="s2" x="713" y="138" width="7" height="7"/><text class="legend-text" x="723" y="147">Sample 2</text>
      <rect class="s3" x="800" y="138" width="7" height="7"/><text class="legend-text" x="810" y="147">Sample 3</text>
    </g>
    <g class="grid">
      <line class="grid-line" x1="418" y1="169" x2="418" y2="531"/>
      <line class="grid-line" x1="581.75" y1="169" x2="581.75" y2="531"/>
      <line class="grid-line" x1="745.5" y1="169" x2="745.5" y2="531"/>
      <line class="grid-line" x1="909.25" y1="169" x2="909.25" y2="531"/>
      <line class="grid-line" x1="1073" y1="169" x2="1073" y2="531"/>
      <line class="grid-line" x1="418" y1="531.5" x2="1073" y2="531.5"/>
    </g>
    <g class="bars">
      <rect class="s1" x="457" y="271.3" width="18" height="259.7"/>
      <rect class="s2" x="491" y="386" width="18" height="145"/>
      <rect class="s3" x="524" y="410.2" width="18" height="120.8"/>
      <rect class="s1" x="620.75" y="380" width="18" height="151"/>
      <rect class="s2" x="654.75" y="265.2" width="18" height="265.8"/>
      <rect class="s3" x="687.75" y="410.2" width="18" height="120.8"/>
      <rect class="s1" x="784.5" y="319.6" width="18" height="211.4"/>
      <rect class="s2" x="818.5" y="422.3" width="18" height="108.7"/>
      <rect class="s3" x="851.5" y="349.8" width="18" height="181.2"/>
      <rect class="s1" x="948.25" y="259.2" width="18" height="271.8"/>
      <rect class="s2" x="982.25" y="361.9" width="18" height="169.1"/>
      <rect class="s3" x="1015.25" y="229" width="18" height="302"/>
    </g>
    <g class="values">
      <text class="value-label" transform="translate(470,265) rotate(-90)">4,3</text>
      <text class="value-label" transform="translate(504,380) rotate(-90)">2,4</text>
      <text class="value-label" transform="translate(537,404) rotate(-90)">2</text>
      <text class="value-label" transform="translate(634,374) rotate(-90)">2,5</text>
      <text class="value-label" transform="translate(668,259) rotate(-90)">4,4</text>
      <text class="value-label" transform="translate(701,404) rotate(-90)">2</text>
      <text class="value-label" transform="translate(797,313) rotate(-90)">3,5</text>
      <text class="value-label" transform="translate(831,416) rotate(-90)">1,8</text>
      <text class="value-label" transform="translate(864,344) rotate(-90)">3</text>
      <text class="value-label" transform="translate(961,253) rotate(-90)">4,5</text>
      <text class="value-label" transform="translate(995,356) rotate(-90)">2,8</text>
      <text class="value-label" transform="translate(1028,223) rotate(-90)">5</text>
    </g>
    <g class="categories">
      <text class="category-label" x="500" y="553" text-anchor="middle">CATEGORY 1</text>
      <text class="category-label" x="663.6" y="553" text-anchor="middle">CATEGORY 2</text>
      <text class="category-label" x="827.4" y="553" text-anchor="middle">CATEGORY 3</text>
      <text class="category-label" x="991.1" y="553" text-anchor="middle">CATEGORY 4</text>
    </g>
  </svg>

  <div class="accent-bar"></div>
  <div class="slide-footer">Footer</div>
  <div class="page-number">4</div>
</main>
</body>
</html>
```